Word Template Designs for Offensive Security Professional Services Report

We need a Microsoft Word Template designed for our Offensive Security professional services reports which includes the following services:

RedTeaming
Network Penetration Testing
Web Application Penetration Testing
Wireless Penetration Testing
Social Engineering

The templates should include the following:
Cover Page design with our Logo included
Executive Summary Page design
Detailed Findings Page design
Design for Last Page

Lastly, I would also like a template I can use for all of my Statements of Work

Requirements
Must have
• Beautiful Eye Catching HD pictures that represent my Offensive Security projects
The design should flow well with our logo

```html
<!DOCTYPE html>
<html lang="en">
<head>
<meta charset="utf-8">
<title>Scope of Work Template Pages</title>
<link href="https://fonts.googleapis.com/css2?family=Source+Sans+3:wght@400;600;700;800&display=swap" rel="stylesheet">
<style>
:root{
  --stage:#5e5e5e;
  --paper:#ffffff;
  --green:#4f9a38;
  --ink:#231f20;
  --muted:#555555;
  --rule:#c9c9c9;
  --night:#0b1a2a;
  --circuit:#1c5d78;
}
*{box-sizing:border-box;margin:0;padding:0}
html,body{width:1200px;height:3000px;overflow:hidden}
body{background:var(--stage);font-family:"Source Sans 3",Arial,sans-serif;color:var(--ink);position:relative}
.page{position:absolute;width:379px;height:535px;background:var(--paper);overflow:hidden}
.col-a{left:200px}.col-b{left:616px}
.row-1{top:83px}.row-2{top:662px}.row-3{top:1232px}.row-4{top:1801px}.row-5{top:2374px}
.content{position:absolute;left:20px;right:20px;top:28px;font-size:5.2px;line-height:1.35}
.title{font-size:20px;font-weight:800;letter-spacing:-.2px;line-height:1;text-transform:uppercase}
.title .accent,.heading .accent{color:var(--green)}
.heading{font-size:11px;font-weight:800;text-transform:uppercase;margin:10px 0 4px;line-height:1.1}
.heading.small{font-size:9.5px}
p{margin-bottom:4px}
ul.bullets{list-style:none;padding-left:6px}
ul.bullets li{position:relative;padding-left:5px;margin-bottom:1.6px}
ul.bullets li::before{content:"";position:absolute;left:0;top:2px;width:2px;height:2px;border-radius:50%;background:var(--ink)}
ul.sub{list-style:none;padding-left:14px}
ul.sub li{position:relative;padding-left:5px;margin-bottom:1.4px}
ul.sub li::before{content:"o";position:absolute;left:0;top:0;font-size:4.5px}
.green-text{color:var(--green)}
.footer-num{position:absolute;left:16px;bottom:18px;font-size:4.5px;color:var(--muted)}
.footer-web{position:absolute;right:16px;bottom:16px;font-size:5.5px;color:var(--green)}

/* cover */
.cover-art{position:absolute;inset:0}
.brand{display:flex;flex-direction:column;align-items:center;gap:3px}
.brand .mark{width:30px;height:30px;border-radius:50%;background:var(--ink)}
.brand .name{font-size:10px;font-weight:700;color:var(--green)}
.cover .brand{position:absolute;left:150px;top:20px}
.cover-title{position:absolute;left:30px;top:102px;width:320px}
.cover-title .kicker{font-size:13px;font-weight:700;color:var(--green)}
.cover-title h1{font-size:15.5px;font-weight:700;line-height:1.2}
.cover-title .for{margin-top:12px;font-size:10.5px;font-weight:600;line-height:1.25}
.prepared{position:absolute;left:30px;top:354px;color:#fff;font-size:6.4px;line-height:1.3}
.prepared .label{font-size:10.5px;font-weight:700}
.prepared .gap{height:6px}
.cover-web{position:absolute;left:30px;bottom:20px;color:var(--green);font-size:6.2px;letter-spacing:.8px;font-weight:600}

/* signature */
.sign{position:absolute;right:20px;width:200px;font-size:4.5px;display:flex;gap:4px}
.sign span.line{flex:1;border-bottom:.6px dotted var(--muted)}

/* revision */
.rev-table{width:100%;border-collapse:collapse;margin-top:14px;font-size:8.5px}
.rev-table th{color:var(--green);font-weight:400;text-align:left;padding:4px 8px;border-top:.6px solid var(--rule);border-bottom:.6px solid var(--rule)}
.rev-table td{font-size:5px;padding:3px 8px 3px 36px}
.rev-table th:last-child{text-align:right}
.rev-table td:last-child{text-align:right;padding-right:30px}

/* toc */
.toc .brand{position:absolute;right:16px;top:18px}
.toc-list{list-style:none;margin-top:18px}
.toc-list li{display:flex;justify-content:space-between;font-size:5.2px;border-bottom:.6px solid var(--rule);padding:5.5px 2px 4px}
.toc-list li.strong{font-weight:700}

/* proposal checks */
.checks{display:grid;grid-template-columns:1fr 1fr;gap:3px 10px;padding-left:6px;margin:3px 0 6px}
.checks span::before{content:"✓ ";color:var(--green)}
.dots{display:grid;grid-template-columns:1fr 1fr;gap:3px 14px;padding-left:24px;margin:4px 0 6px}
.dots span{position:relative;padding-left:8px}
.dots span::before{content:"";position:absolute;left:0;top:1px;width:3.5px;height:3.5px;border-radius:50%;background:var(--green)}
.note{font-size:4.6px}

/* tasks */
.tasks{padding-left:8px}
.tasks .stage{margin-top:4px}
.tasks .stage b{font-weight:700}
.tasks .step{margin-top:1px}
.tasks ul{list-style:none;padding-left:24px}
.tasks ul li::before{content:"• "}
</style>
</head>
<body>

<!-- Cover -->
<section class="page cover col-a row-1">
  <svg class="cover-art" width="379" height="535" viewBox="0 0 379 535" aria-hidden="true">
    <defs>
      <linearGradient id="nightGlow" x1="0" y1="0" x2="1" y2="1">
        <stop offset="0" stop-color="#123a55"/>
        <stop offset=".55" stop-color="#0d2436"/>
        <stop offset="1" stop-color="#050d16"/>
      </linearGradient>
    </defs>
    <polygon points="0,318 379,170 379,180 0,333" fill="var(--green)"/>
  </svg>
  <svg class="cover-art" width="379" height="535" viewBox="0 0 379 535" role="img" aria-label="Photo of a glowing circuit board with a padlock shield emblem and a hand touching it">
    <polygon points="0,333 379,180 379,535 0,535" fill="url(#nightGlow)"/>
  </svg>
  <div class="brand"><span class="mark"></span><span class="name">Vantage Cyber</span></div>
  <div class="cover-title">
    <div class="kicker">SCOPE OF WORK :</div>
    <h1>External, Internal Network,<br>Wireless and Web Application Penetration<br>Testing Engagement</h1>
    <div class="for">PREPARED FOR :<br><span style="font-weight:400">[Client Name]</span></div>
  </div>
  <div class="prepared">
    <div class="label">PREPARED BY :</div>
    Daniel Marlow, CISSP, OSCE, OSCP<br>[Company Name], LLC
    <div class="gap"></div>
    4210 Harbor Lane Suite 210<br>Austin Texas 78701<br>www.vantage-cyber.example
    <div class="gap"></div>
    Daniel.Marlow@vantage-cyber.example<br>Office 800.555.0142<br>Mobile: 512.555.0187<br>August 2, 2018
  </div>
  <div class="cover-web">www.vantage-cyber.example</div>
</section>

<!-- Scope approval -->
<section class="page col-b row-1">
  <div class="content" style="top:26px">
    <div class="title"><span class="accent">Scope</span> Approval</div>
    <div class="heading small" style="margin-top:8px"><span class="accent">Client Activity</span> Checklist</div>
    <ul class="bullets">
      <li>Provide access to client's facilities, as required.</li>
      <li>Provide access to client's existing policy documentation.</li>
      <li>Provide access to client's intranet portal.</li>
      <li>Provide workspace and Internet connections for [Company Name] consultants for any on-site activities.</li>
      <li>Provide access to client's technical staff (e.g. network administrators, security officers, database administrators, etc.), or such knowledgeable personnel who can provide the necessary answers to questions regarding the current network environment, current and future business objectives, security practices, etc.</li>
      <li>Provide access to the following information, documentation (as required):</li>
    </ul>
    <ul class="sub">
      <li>Policies, Standards, Guidelines, Procedures relevant to this work.</li>
      <li>Any other reasonable information deemed necessary by [Company Name] for the successful completion of this engagement.</li>
      <li>Facilitate communication with Telco, ISP or other connected sites as needed.</li>
    </ul>
    <ul class="bullets"><li>Provide a single point of contact that will be responsible for:</li></ul>
    <ul class="sub">
      <li>Arrangements and clearances from client management</li>
      <li>Delivery of necessary information to [Company Name] to complete the project</li>
      <li>Approvals to scope of work changes (including acceptance of additional billing)</li>
      <li>Interfaces with client project management or change management to secure adequate maintenance windows to perform work as needed</li>
      <li>Approve project delivery based on defined success criteria.</li>
    </ul>
    <div class="heading small"><span class="accent">Acknowledgements</span></div>
    <p>[Company Name] will work with the client during the course of this project to ensure that each of the phases and tasks are complete as described herein and that [Company Name] completes all of the deliverables listed in this document.</p>
    <p>Any additional deliverables and/or changes to the project task list or phases are considered changes in the scope of work. Such changes require a new scope of work to be issued and signed. Changes that exceed twenty percent (20%) of the total original project cost will require the issuance of a purchase order or some other form of pre-payment.</p>
    <p>The solution described in this document is based on [Company Name] current understanding of the client's environment, business, and technical requirements. Any changes could affect the project cost and/or schedule. Any timelines or dates in this document are best estimates only.</p>
    <p>A purchase order must be issued to [Company Name] before the project can be scheduled and resources assigned.</p>
    <p>I acknowledge receipt and acceptance of this project scope of work.</p>
  </div>
  <div class="sign" style="top:460px">Client Signature <span class="line"></span></div>
  <div class="sign" style="top:480px">Date <span class="line"></span></div>
  <div class="sign" style="top:500px">Client Name <span class="line"></span></div>
  <div class="footer-num">Page 16</div>
</section>

<!-- Revision control -->
<section class="page col-a row-2">
  <div class="content" style="top:20px;left:14px;right:18px">
    <div class="title" style="text-align:center;font-size:17px"><span class="accent">Document Revision</span> Control</div>
    <table class="rev-table">
      <tr><th>Revision Number</th><th style="text-align:center">Revision</th><th>Revision Date</th></tr>
      <tr><td>1.0</td><td style="padding-left:0;text-align:center">Initial</td><td>8/2/18</td></tr>
    </table>
  </div>
  <div class="footer-num">Page 2</div>
</section>

<!-- Table of contents -->
<section class="page toc col-b row-2">
  <div class="brand"><span class="mark"></span><span class="name">Vantage Cyber</span></div>
  <div class="content" style="top:114px;left:12px;right:18px">
    <div class="title"><span class="accent">Table of</span> Contents</div>
    <ul class="toc-list">
      <li class="strong"><span>TABLE OF CONTENTS</span><span>3</span></li>
      <li class="strong"><span>PROPOSAL SUMMARY</span><span>4</span></li>
      <li><span>ENGAGEMENT OVERVIEW</span><span>4</span></li>
      <li><span>Phase One: External Network Penetration Testing</span><span>4</span></li>
      <li><span>Phase Two: Internal Network Penetration Testing</span><span>4</span></li>
      <li><span>Phase Three: Wireless Penetration Testing</span><span>5</span></li>
      <li><span>Phase Four: Targeted Web Application Penetration Testing</span><span>5</span></li>
      <li><span>ENGAGEMENT DELIVERABLES</span><span>6</span></li>
      <li><span>PHASE SPECIFIC TASKS</span><span>7</span></li>
      <li><span>Phase One: External Network Penetration Testing</span><span>7</span></li>
      <li><span>Phase Two: Internal Network Penetration Testing</span><span>9</span></li>
      <li><span>Phase Three: Wireless Penetration Testing</span><span>11</span></li>
      <li><span>Phase Four: Targeted Web Application Penetration Testing</span><span>12</span></li>
      <li class="strong"><span>ABOUT [COMPANY NAME]</span><span>15</span></li>
      <li><span>CONSULTANT PROFILE</span><span>15</span></li>
      <li class="strong"><span>SCOPE APPROVAL</span><span>16</span></li>
      <li><span>CLIENT ACTIVITY CHECKLIST</span><span>16</span></li>
      <li><span>ACKNOWLEDGEMENTS</span><span>16</span></li>
    </ul>
  </div>
  <div class="footer-num">Page 3</div>
</section>

<!-- Proposal summary -->
<section class="page col-a row-3">
  <div class="content" style="top:26px;left:12px;right:16px">
    <div class="title"><span class="accent">Proposal</span> Summary</div>
    <p style="margin-top:4px">[Company Name] is proud to present this multi-phase Scope of Work to [Client Name] to meet their Penetration Testing Requirements. [Company Name] LLC's security consultants have expert knowledge in Network Security and Web Applications, Security Controls, process and procedures, best practices, vulnerabilities and countermeasures. Our security consultants will perform the penetration testing presented in this Scope of Work.</p>
    <div class="heading small" style="margin-top:14px"><span class="accent">Engagement</span> Overview</div>
    <p>Based on the information provided, [Company Name] understands that [Client Name] objectives are to have [Company Name] LLC provide penetration testing, ethical hacking and risk management services to [Client Name] to help ensure that the systems are working in a safe secure manner in every respect and by ensuring the proper preservation of all data's Confidentiality, Integrity, and Availability (CIA).</p>
    <p>From [Company Name]'s understanding, [Client Name] has requested that the penetration testing be performed from a grey box perspective to determine the exposed vulnerabilities of the networks, applications and wireless implementations.</p>
    <p class="green-text" style="margin-top:6px">In response to these requirements, [Company Name] will perform the following services :</p>
    <div class="checks">
      <span>External Network Penetration Testing</span><span>Internal Network Penetration Testing</span>
      <span>Wireless Network Penetration Testing</span><span>Targeted Web Application Penetration Testing</span>
    </div>
    <div class="heading small">Phase One: <span class="accent">External Network Penetration Testing</span></div>
    <p>[Company Name] will conduct a Network Penetration Testing assessment of the external network, aka the Internet presence to help identify existing vulnerabilities and their associated risks. [Company Name] will discover and identify hosts belonging to [Client Name] external network, identify vulnerabilities and exploit vulnerabilities identified during the ethical hacking process. After a system is compromised, the vulnerabilities and any applicable exploits will be documented in a detailed, repeatable process.</p>
    <p>[Company Name] will conduct this work remotely while performing the Network Penetration Testing assessment in collaboration with [Client Name] personnel. After the assessment is complete, [Company Name] will develop a formal report that will include the items described in the Final Report Summary.</p>
    <div class="heading small">Phase Two: <span class="accent">Internal Network Penetration Testing</span></div>
    <p>[Company Name] will conduct a penetration test of the [Client Name] internal network, aka their private LAN. [Company Name] will exploit vulnerabilities identified during the vulnerability identification process. After a system is compromised, the vulnerabilities and any applicable exploits will be documented in a detailed, repeatable process.</p>
    <p>[Company Name] will conduct this work onsite initially and remotely after deploying [Company Name]'s internal network attack server. The Network Penetration Testing will be conducted in collaboration with [Client Name] personnel. After the assessment is complete, [Company Name] will develop a formal report that will include the items described in the Final Report Summary.</p>
    <p class="note"><b>Note :</b> The attack server's purpose is to facilitate internal network penetration testing efforts from a remote offsite location. This will help emulate an attacker who has gained access to the internal network and is outside of the organization. No Denial of Service or testing outside of the internal network penetration testing efforts will be conducted via the attack server.</p>
  </div>
  <div class="footer-num">Page 4</div>
  <div class="footer-web">www.vantage-cyber.example</div>
</section>

<!-- Phase three / four -->
<section class="page col-b row-3">
  <div class="content" style="top:18px;left:16px;right:16px">
    <div class="heading small" style="margin-top:0">Phase Three: <span class="accent">Wireless Penetration Testing</span></div>
    <p>[Company Name] will assess [Client Name] guest and production wireless networks. During testing, [Company Name] will attempt to gain access to hosts belonging to [Client Name] internal network presence and wireless controllers. [Company Name] will exploit vulnerabilities identified during the vulnerability identification process. After a system or information is compromised, [Company Name] will gather appropriate evidence for proof of information or system compromise.</p>
    <p>[Company Name] will conduct this work on-site while performing the assessment in collaboration with [Client Name]. After the assessment is complete, [Company Name] will develop a formal report that will include the items described in the Final Report Summary.</p>
    <div class="heading small">Phase Four: <span class="accent">Targeted Web Application<br>Penetration Testing</span></div>
    <p>[Company Name] will conduct a Targeted Web Application Penetration Testing assessment of the target web application and supporting services as an unauthorized/unauthenticated and authorized/authenticated user's perspective to determine the exposed vulnerabilities that are accessible to an attacker.</p>
    <p><span class="green-text">Unauthorized/Unauthenticated</span> – An Unauthenticated Assessment of your web application gives a realistic view of what an attacker with a simple Internet connection and no privileges would be able to access, find, and possibly exploit. This type of assessment tests the strengths of your application's authentication mechanism(s) and any other vulnerability associated with the application.</p>
    <p><span class="green-text">Authorized/Authenticated</span> – An Authenticated Assessment of your web application gives a realistic view of what an attacker with basic and administrative privileges would be able to access, find, and possibly exploit. This type of assessment tests the strengths of your applications to withstand attacks by authorized users who have valid credentials to authenticate to the application.</p>
    <p>Additional testing may include the following :</p>
    <div class="dots">
      <span>Information Leakage</span><span>OS Command Injection</span>
      <span>Session Management</span><span>Local and Remote File Inclusion</span>
      <span>Default Configurations</span><span>Cross Site Request Forgery</span>
      <span>Authentication abuse</span><span>Application and Business Logic Flaws</span>
      <span>Client-Side Cache</span><span>Proper Input Validation</span>
      <span>Authorization exploitation</span><span>Privilege Escalation Opportunities</span>
      <span>SQL Injection, (backend database enumeration and manipulation)</span><span>Client-Side Code<br><br>Server-Side Input Validation</span>
    </div>
    <p>[Company Name] follows a well-developed and proven methodology to assess the security of web-based applications as defined in the specific tasks in the next section. After the assessment is complete, [Company Name] will develop a formal report that will include the items described in the Final Report Summary.</p>
    <div class="heading small" style="margin-top:8px"><span class="accent">Engagement</span> Deliverables</div>
    <p>[Company Name] will provide the following Deliverables to [Client Name]:</p>
    <ul class="dots" style="display:block;padding-left:6px;list-style:none">
      <li style="margin-bottom:4px"><span>Weekly Status Updates if applicable</span></li>
      <li style="margin-bottom:4px"><span>Final Report and Presentation delivered at the end of the engagement</span></li>
      <li><span>Onsite Q&amp;A session with our consultants to discuss the process, findings, and recommendations, and answer questions related to the engagement.</span></li>
    </ul>
  </div>
  <div class="footer-num">Page 5</div>
  <div class="footer-web">www.vantage-cyber.example</div>
</section>

<!-- Phase specific tasks: phase one -->
<section class="page col-a row-4">
  <div class="content" style="top:22px;left:16px;right:16px">
    <div class="title"><span class="accent">Phase Specific</span> Tasks</div>
    <p style="margin-top:3px">This engagement consists of four phases which break down into the following tasks and milestones.</p>
    <div class="heading small" style="margin-top:6px">Phase One: <span class="accent">External Network Penetration Testing</span></div>
    <div class="tasks">
      Duration: [Timeframe]<br>Consultant Presence: 100% Remote<br>Client Time Commitment: 1 - 2 staff hours<br>The goal of this assessment is to conduct a Penetration Test of [Client Name] Internet Presence.<br>This consulting engagement consists of four stages:
      <div class="stage"><b>Stage 1:</b> Project/Phase Kickoff</div>
      <ul><li>Identify Stakeholders and responsible parties</li><li>Establish Timelines</li><li>Identify sources of required information</li></ul>
      <div class="stage"><b>Stage 2:</b> External Network Ethical Hacking</div>
      <div class="step">1. Determine and validate specified IP addresses to be tested based on information supplied by the client.</div>
      <div class="step">2. Gather public information about the organization such as but not limited to:</div>
      <ul><li>Employee names, phone numbers and email addresses</li><li>Computer account naming conventions</li><li>Domain registry information</li><li>Help Desk information and support procedures</li></ul>
      <div class="step">3. Gather specific information such as:</div>
      <ul><li>Information from DNS servers about organizational systems</li><li>Information derived from email transfers</li><li>Trace route information to organization systems</li></ul>
      <div class="step">4. Use port scanners to determine the following information:</div>
      <ul><li>Ports and services available on the information systems</li><li>Web, Mail, DNS, Firewall, Routers, Switches address information</li><li>Operating system, and application versioning information</li></ul>
      <div class="step">5. Use service specific tools to gather additional information from server about user configurations</div>
      <div class="step">7. Conduct a vulnerability scan of exposed system and services and create a prioritized list of exploits for use.</div>
      <div class="step">8. Check for common administrative misconfigurations such as:</div>
      <ul><li>Common and default system service accounts</li><li>Default usernames and passwords</li><li>Default community strings (SNMP)</li><li>Mail relay allowed on SMTP servers</li></ul>
      <div class="step">9. Perform password-based attacks on:</div>
      <ul><li>Servers (telnet, FTP, SMB VNC, MSRDP, basic authentication etc)</li><li>Routers (telnet, SSH and community strings)</li></ul>
      <div class="stage"><b>Stage 3:</b> Early Warning Notification</div>
      <ul><li>Review Vulnerability, Threat Vectors, Exploits and Possible Countermeasures.</li></ul>
      <div class="stage"><b>Stage 4:</b> Data Analysis and Draft Report</div>
      <ul><li>Data Analysis</li><li>Draft Report Creation</li></ul>
    </div>
  </div>
  <div class="footer-num">Page 6</div>
  <div class="footer-web">www.vantage-cyber.example</div>
</section>

<!-- Client obligations 1 -->
<section class="page col-b row-4">
  <div class="content" style="top:18px;left:16px;right:16px">
    <div class="heading small" style="margin-top:0"><span class="accent">Client</span> Obligations</div>
    <p>Working Sessions will be conducted during both on-site meeting and via [Company Name] provided web-based collaboration / teleconferences and will require extensive interaction with the client, as detailed by meeting schedule below. The client will be required to provide access to IT managers, IT Staff in order to define the basic data sets and elements.</p>
    <div class="heading small" style="margin-top:10px"><span class="accent">Meeting</span> Schedules</div>
    <p>• <u>Phase One kick-off</u> (30 minutes) to establish a timeline and review client requirements.</p>
    <p>• Final Report will be presented at the end of the assessment.</p>
  </div>
  <div class="footer-num">Page 7</div>
  <div class="footer-web">www.vantage-cyber.example</div>
</section>

<!-- Phase two tasks -->
<section class="page col-a row-5">
  <div class="content" style="top:20px;left:16px;right:16px">
    <div class="heading small" style="margin-top:0">Phase Two: <span class="accent">Internal Network Penetration Testing</span></div>
    <div class="tasks">
      Timeline: [Timeframe]<br>Consultant Presence: 25% Onsite, 75% Remote<br>Client Time Commitment: 3 - 4 staff hours<br>The goal of this phase is to conduct an ethical hacking exercise on [Client Name]' Internal network in a collaborative fashion.<br>This phase of the consulting engagement consists of three stages:
      <div class="stage"><b>Stage 1:</b> Project/Phase Kickoff</div>
      <ul><li>Identify Stakeholders and responsible parties</li><li>Establish Timelines</li><li>Identify sources of required information</li></ul>
      <div class="stage"><b>Stage 2:</b> Internal Network Ethical Hacking</div>
      <div class="step">1. Determine and validate specified IP addresses to be tested based on information supplied by the client.</div>
      <div class="step">2. Gather public information about the organization such as but not limited to:</div>
      <ul><li>Employee names, phone numbers and email addresses</li><li>Computer account naming conventions</li><li>Domain registry information</li><li>Help Desk information and support procedures</li></ul>
      <div class="step">3. Gather specific information such as:</div>
      <ul><li>Information from DNS servers about organizational systems</li><li>Information derived from email transfers</li><li>Trace route information to organization systems</li></ul>
      <div class="step">4. Use port scanners to determine the following information:</div>
      <ul><li>Ports and services available on the information systems</li><li>Web, Mail, DNS, Firewall, Routers, Switches address information</li><li>Operating system, and application versioning information</li></ul>
      <div class="step">5. Use service specific tools to gather additional information from server about user configurations</div>
      <div class="step">6. Conduct a vulnerability scan of exposed system and services and create a prioritized list of exploits for use.</div>
      <div class="step">7. Check for common administrative misconfigurations such as:</div>
      <ul><li>Common and default system service accounts</li><li>Default usernames and passwords</li><li>Default community strings (SNMP)</li><li>Mail relay allowed on SMTP servers</li></ul>
      <div class="step">8. Perform password based attacks on:</div>
      <ul><li>Servers (telnet, FTP, SMB VNC, MSRDP, basic authentication etc)</li><li>Routers (telnet, SSH and community strings)</li></ul>
      <div class="stage"><b>Stage 3:</b> Data Analysis and Draft Report</div>
      <ul><li>Data Analysis</li><li>Draft Report Creation</li></ul>
    </div>
  </div>
  <div class="footer-num">Page 8</div>
  <div class="footer-web">www.vantage-cyber.example</div>
</section>

<!-- Client obligations 2 -->
<section class="page col-b row-5">
  <div class="content" style="top:18px;left:16px;right:16px">
    <div class="heading small" style="margin-top:0"><span class="accent">Client</span> Obligations</div>
    <p>Working Sessions will be conducted during both on-site meeting and via [Company Name] provided web-based collaboration / teleconferences and will require extensive interaction with the client, as detailed by meeting schedule below. The client will be required to provide access to IT managers, IT Staff in order to define the basic data sets and elements.</p>
    <div class="heading small" style="margin-top:10px"><span class="accent">Meeting</span> Schedules</div>
    <p>• <u>Phase Two kick-off</u> (30 minutes) to establish a timeline and review client requirements.</p>
    <p>• Final Report will be presented at the end of the assessment.</p>
  </div>
  <div class="footer-num">Page 9</div>
  <div class="footer-web">www.vantage-cyber.example</div>
</section>

</body>
</html>
```